VORLAX POSTCARD

I submitted my postcard and printer said it is not acceptable here are the comments
Item 125301 - Front file: Uploaded png is 3.3 x 2.2" at 300 dpi. Back file: Uploaded png is 5 x 3.3" at 200 dpi. There is text and images too close to the edges for the front and back. Both front/back files are low resolution and have poor print quality. The correct size for a jumbo postcard is 8.75 x 5.75". The intended bleed extends to the edges and all important text and/or elements are to remain at least 3/8" away from the edges. Try saving as a PDF from the source file at the correct size for a possible better printing output.

Item 125302 - Front file: Uploaded jpg is 7 x 5" at 200 dpi. Back file: Uploaded jpg is 8 x 5" at 220 dpi. Both front/back files are low resolution and have poor print quality. The correct size for a Medium QTVR card is 8.25 x 6.75" The intended bleed extends to the edges of the canvas and all important text and/or elements are to remain at least 3/8" away from the edges. Try saving as a PDF from the source file at the correct size for a possible better printing output.

```html
<!DOCTYPE html>
<html lang="en">
<head>
<meta charset="utf-8">
<title>Vorlax Postcard</title>
<link href="https://fonts.googleapis.com/css2?family=Lato:wght@300;400;700&family=Poppins:ital,wght@0,600;0,700;0,800;1,600&display=swap" rel="stylesheet">
<style>
:root{
  --stage:#1b1b1d;
  --red:#c62026;
  --yellow:#f4d823;
  --gold:#e9b735;
  --blue:#2273b8;
  --blue-deep:#2467a8;
  --blue-light:#2f86cc;
  --ink:#222;
  --paper:#ffffff;
  --mist:#f3f3f3;
}
*{margin:0;padding:0;box-sizing:border-box}
html,body{width:1200px;height:1200px;overflow:hidden;background:var(--stage)}
.card{position:absolute;left:236px;width:728px;height:471px;overflow:hidden;font-family:"Lato",sans-serif}
.card--front{top:109px;background:var(--paper)}
.card--back{top:620px;background:var(--mist)}
.shapes{position:absolute;inset:0}
.abs{position:absolute}

/* front */
.tagline{left:180px;top:12px;font-family:"Lato",sans-serif;font-size:15px;line-height:16px}
.tagline .lang{color:var(--red);font-weight:400}
.tagline .tele{color:var(--ink);font-weight:700}
.portrait{left:12px;top:37px;width:140px;height:140px;border-radius:50%;background:radial-gradient(circle at 50% 45%,#e8c9b4 0%,#c9a894 40%,#5fb0c6 75%,#4aa3bb 100%)}
.doctor-name{left:165px;top:94px;font-family:"Poppins",sans-serif;font-weight:800;font-size:23px;line-height:24px;color:#fff;letter-spacing:.5px}
.headline{left:0;width:364px;top:196px;text-align:center}
.headline .cares{font-family:"Poppins",sans-serif;font-weight:700;font-size:23px;color:var(--blue);line-height:28px}
.headline .trust{font-family:"Lato",sans-serif;font-weight:300;font-size:23px;color:var(--red);line-height:26px}
.bio{left:26px;top:266px;width:313px;color:#fff;font-size:12.4px;line-height:15.6px;text-align:justify}
.bio p+p{margin-top:10px;text-align:left}
.services{left:441px;top:158px}
.services h3{font-family:"Lato",sans-serif;font-weight:700;color:var(--red);font-size:13.5px;line-height:16px}
.services ul{list-style:none;margin-top:10px}
.services li{font-size:12.4px;line-height:17.2px;color:var(--blue);padding-left:17px;position:relative}
.services li::before{content:"";position:absolute;left:2px;top:7px;width:4px;height:4px;border-radius:50%;background:var(--blue)}
.address{left:420px;width:260px;top:424px;text-align:center;font-weight:700;font-size:12.6px;line-height:16px;color:var(--ink)}
.indicia{border:1px solid #555;background:#fff;font-family:Arial,sans-serif;color:#333}
.indicia--route{left:494px;top:12px;width:135px;height:47px;font-size:6.4px;padding:12px 5px 0}
.indicia--route .code{text-align:center;margin-bottom:4px}
.indicia--postage{left:633px;top:12px;width:82px;height:47px;font-size:5.8px;text-align:center;padding-top:8px;line-height:8px}
.indicia--postage .site{font-size:4.2px}

/* back */
.back-title{left:0;width:281px;top:58px;text-align:center;font-family:"Poppins",sans-serif;font-weight:800;color:#fff;font-size:18px;line-height:26px;letter-spacing:-.3px}
.photo{left:57px;width:166px;border:1px solid #ccc}
.photo--front{top:117px;height:105px;background:linear-gradient(180deg,#3f5a4d 0%,#8a8f86 45%,#c9c9c4 100%)}
.photo--lobby{top:231px;height:104px;background:linear-gradient(180deg,#d9e6e8 0%,#b8c6c8 55%,#6e7476 100%)}
.brand{left:500px;top:26px;display:flex;align-items:center;gap:10px}
.brand .dot{width:22px;height:22px;border-radius:50%;background:var(--gold)}
.brand .word{font-family:"Poppins",sans-serif;font-weight:700;font-size:38px;color:var(--blue);letter-spacing:1px}
.perks{left:310px;top:100px;width:410px;list-style:none}
.perks li{position:relative;padding-left:21px;font-family:"Poppins",sans-serif;font-weight:700;font-size:13.6px;line-height:17px;margin-bottom:4px}
.perks li.b{color:var(--blue)}
.perks li.r{color:var(--red)}
.perks li svg{position:absolute;left:0;top:4px}
.perks .note{display:block;font-weight:600;font-style:italic;font-size:10.6px;line-height:14px;margin-top:1px}
.phone{left:444px;top:323px;display:flex;align-items:center;gap:8px;font-family:"Poppins",sans-serif;font-weight:800;font-size:20px;color:var(--ink);letter-spacing:.5px}
.insurers{left:0;top:356px;width:728px;height:99px;background:#fff}
.insurer-row{position:absolute;left:30px;width:588px;display:flex;align-items:center;justify-content:space-between}
.insurer-row--top{top:14px;height:30px}
.insurer-row--bottom{top:54px;height:34px}
.insurer{font-family:"Poppins",sans-serif;font-weight:700;font-size:10px;display:flex;align-items:center;gap:4px;white-space:nowrap}
.insurer--large{font-size:15px}
.insurer i{display:inline-block;width:9px;height:9px;flex:none}
.badge{width:52px;height:28px;background:#d8d8d8;flex:none}
.cash{position:absolute;left:628px;top:15px;width:86px;text-align:center;font-family:"Lato",sans-serif;font-weight:700;color:var(--red);font-size:11.5px;line-height:14.6px}
.band-blue{left:0;top:455px;width:331px;height:16px;background:var(--blue-deep)}
.band-gold{left:331px;top:455px;width:397px;height:16px;background:var(--gold)}
</style>
</head>
<body>

<section class="card card--front">
  <svg class="shapes" width="728" height="471" viewBox="0 0 728 471">
    <polygon points="364,302 728,130 728,471 364,471" fill="#f3f3f3"/>
    <polygon points="0,0 161,0 161,50 364,50 364,184 199,184 0,93" fill="#c62026"/>
    <polygon points="161,0 503,0 364,68 364,50 161,50" fill="#f4d823"/>
    <defs>
      <linearGradient id="bioPanel" x1="0" y1="1" x2="1" y2="0">
        <stop offset="0" stop-color="#2467a8"/>
        <stop offset="1" stop-color="#2f86cc"/>
      </linearGradient>
    </defs>
    <rect x="0" y="253" width="364" height="218" fill="url(#bioPanel)"/>
    <polygon points="0,253 364,253 364,300 0,440" fill="#2a76bd" opacity=".6"/>
  </svg>

  <div class="abs tagline"><div class="lang">SE’ HABLA ESPANOL</div><div class="tele">TELE-VISITS AVAILABLE</div></div>
  <div class="abs portrait" role="img" aria-label="Portrait photo of Dr. Marisol Varenne"></div>
  <div class="abs doctor-name">MARISOL<br>VARENNE, MD</div>

  <div class="abs headline">
    <div class="cares">A DOCTOR WHO CARES</div>
    <div class="trust">EXPERIENCE YOU CAN TRUST</div>
  </div>

  <div class="abs bio">
    <p><b>Dr. Varenne</b> has been practicing medicine in Halbrook for over 12 years. She was previously a primary care doctor with St. Brennan Eastside Clinic in Halbrook for 10 years. Dr. Varenne became dissatisfied with the assembly line fashion of medical care and the pressure to spend minimal time with patients. Dr. Varenne choose to go out on her own to deliver medical care the way she believes it should be practiced. Dr. Varenne prides herself on delivering the individual care that patients require no matter the time required.</p>
    <p>Dr. Varenne maintains hospital privileges at Northgate/St. Brennan, Ashford, Linwood.</p>
  </div>

  <div class="abs indicia indicia--route"><div class="code">*********ECRWSSQTVR****</div><div>Postal Customer</div></div>
  <div class="abs indicia indicia--postage">PRSRT MKTG<br>U.S. POSTAGE<br>PAID<br><span class="site">MAILPRESSPRINT.EXAMPLE</span></div>

  <div class="abs services">
    <h3>ALL PRIMARY CARE<br>SERVICES INCLUDING</h3>
    <ul>
      <li>Hypertension (High Blood Pressure)</li>
      <li>Diabetes</li>
      <li>Colds</li>
      <li>Flu</li>
      <li>COVID</li>
      <li>Sports Physicals</li>
      <li>Auto Accidents/Slip &amp; Fall</li>
      <li>Blood Tests</li>
      <li>Back /Neck /Knee /Shoulder PAIN</li>
      <li>Vaccinations for Flu, Pneumonia</li>
      <li>Immigration examinations</li>
      <li>Social Security Examinations</li>
    </ul>
  </div>

  <div class="abs address">418 LINDEN AVENUE<br>HALBROOK, NJ 08190 &nbsp;&nbsp;|&nbsp;&nbsp; 555-014-7720</div>
</section>

<section class="card card--back">
  <svg class="shapes" width="728" height="471" viewBox="0 0 728 471">
    <polygon points="0,0 174,0 174,30 200,43 281,43 281,221 57,221 0,160" fill="#2467a8"/>
    <polygon points="174,0 447,0 281,79 281,43 200,43 174,30" fill="#f4d823"/>
  </svg>

  <div class="abs back-title">PRIMARY CARE MEDICINE<br>RIGHT ON LINDEN</div>
  <div class="abs photo photo--front" role="img" aria-label="Photo of the clinic entrance with steps and white railings"></div>
  <div class="abs photo photo--lobby" role="img" aria-label="Photo of the clinic waiting room with chairs"></div>

  <div class="abs brand"><span class="dot"></span><span class="word">VORLAX</span></div>

  <ul class="abs perks">
    <li class="b"><svg width="9" height="8" viewBox="0 0 9 8"><path d="M1 4l2.5 3L8 1" fill="none" stroke="currentColor" stroke-width="1.2"/></svg>ALL INSURANCES ACCEPTED INCLUDING MEDICARE/MEDICAID</li>
    <li class="r"><svg width="9" height="8" viewBox="0 0 9 8"><path d="M1 4l2.5 3L8 1" fill="none" stroke="currentColor" stroke-width="1.2"/></svg>ACCEPTING NEW PATIENTS/IMMEDIATE APPOINMENT AVAILABLE</li>
    <li class="b"><svg width="9" height="8" viewBox="0 0 9 8"><path d="M1 4l2.5 3L8 1" fill="none" stroke="currentColor" stroke-width="1.2"/></svg>FIRST-CLASS STATE OF THE ART OFFICE</li>
    <li class="r"><svg width="9" height="8" viewBox="0 0 9 8"><path d="M1 4l2.5 3L8 1" fill="none" stroke="currentColor" stroke-width="1.2"/></svg>BE SEEN BY BOARD CERTIFIED INTERNAL MEDICINE DOCTOR<span class="note">(The doctor will be available when you need her. No shuffling from doctor-to-doctor Dr. Varenne will be YOUR doctor)</span></li>
    <li class="b"><svg width="9" height="8" viewBox="0 0 9 8"><path d="M1 4l2.5 3L8 1" fill="none" stroke="currentColor" stroke-width="1.2"/></svg>MULTIPLE SPECIALISTS UNDER ONE ROOF<span class="note">(Psychiatry, Podiatry, Chiropractic, Cardiology. Pain Management)</span></li>
    <li class="r"><svg width="9" height="8" viewBox="0 0 9 8"><path d="M1 4l2.5 3L8 1" fill="none" stroke="currentColor" stroke-width="1.2"/></svg>ON SITE BLOOD LABORATORY</li>
  </ul>

  <div class="abs phone">
    <svg width="16" height="16" viewBox="0 0 16 16"><circle cx="8" cy="8" r="8" fill="#111"/><path d="M5.2 4.2l1.3-.4.8 2-1 .8c.5 1.2 1.4 2.1 2.6 2.6l.8-1 2 .8-.4 1.3c-3.6.1-6.2-2.5-6.1-6.1z" fill="#fff"/></svg>
    <span>555-014-7720</span>
  </div>

  <div class="abs insurers">
    <div class="insurer-row insurer-row--top">
      <span class="insurer" style="color:#1f5aa6"><i style="background:#1f5aa6"></i>Crestline Health</span>
      <span class="insurer" style="color:#1f4a8a">Harborview</span>
      <span class="insurer" style="color:#5a7a2a">Tandem</span>
      <span class="insurer" style="color:#1f3f8a">Keystride</span>
      <span class="insurer" style="color:#333">Silvergate Plans</span>
      <span class="insurer" style="color:#1a8ab0"><i style="background:#1a8ab0;border-radius:50%"></i>Brightpath</span>
      <span class="insurer" style="color:#2a4f8f">Oakmere</span>
    </div>
    <div class="insurer-row insurer-row--bottom">
      <span class="insurer" style="color:#1f3f7a">Lumen NJ Health</span>
      <span class="insurer" style="color:#1f3f8a">Pinefield</span>
      <span class="insurer" style="color:#1f3f8a"><i style="background:#1f3f8a"></i>Unity Shield</span>
      <span class="insurer" style="color:#7a3a9a">Corvana</span>
      <span class="insurer" style="color:#1a8a8a">Fairhaven Care</span>
      <span class="badge"></span>
      <span class="insurer insurer--large" style="color:#1a7a5a">Meadowly</span>
      <span class="insurer insurer--large" style="color:#6aaa2a">Halcyon</span>
    </div>
    <div class="cash">CASH<br>PATIENTS<br>WELCOME</div>
  </div>

  <div class="abs band-blue"></div>
  <div class="abs band-gold"></div>
</section>

</body>
</html>
```